Custom Home Page for our new Website

We need a custom home page designed for our new website. We are a successful local copier dealer who is rebuilding our website from scratch. We have decided on Wordpress as our CMS platform and have purchased the professional Corvel theme.

The custom homepage we want will be an imitation of the screen on latest model of copiers we carry. (A picture of this is attached.) the goal is to imitate this style while creating a unique, user-friendly, helpful portal to our website.

The winning entry will make the best transition between the menu structure of our current website (www.hlumo.net) and the new layout.

Target Market(s)

Our target market is small to medium sized businesses in the Southeast US. The users of our site are generally IT professionals looking for drivers/support, gatekeepers or other support staff placing service calls and supply orders or prospects looking for information about our company and products.

Requirements
Must have
• Clean design, no distracting elements
• Modern aesthetic
• A color palette that can be used as a basis for the Skin for the rest of the site (The site's look will be based on the winning homepage design.)
• Simple navigation
• Easy to read
• Easily viewed on both desktop and tablet sized screens
• Our logo
• Easily update-able
• Maximum of 4 of the large squares

```html
<!DOCTYPE html>
<html lang="en">
<head>
<meta charset="utf-8">
<title>Hlumo – Copiers and Support</title>
<link href="https://fonts.googleapis.com/css2?family=Open+Sans:wght@300;400;600;700&display=swap" rel="stylesheet">
<style>
:root{
  --red:#c4122f;
  --ink:#2b2b2b;
  --text:#555;
  --muted:#8a8a8a;
  --line:#dedede;
  --panel:#f3f3f3;
  --band:#ececec;
  --white:#fff;
}
*{box-sizing:border-box;margin:0;padding:0}
html,body{width:768px;height:1200px;overflow:hidden;background:var(--white)}
body{position:relative;font-family:"Open Sans",Arial,sans-serif;color:var(--text)}
.abs{position:absolute}
.top-bar{left:0;top:0;width:768px;height:3px;background:var(--red)}
.top-toggle{left:675px;top:3px;width:18px;height:17px;background:var(--red);color:#fff;font-size:13px;line-height:16px;text-align:center;font-weight:600}
.brand{left:74px;top:32px;display:flex;align-items:center;gap:7px}
.brand-mark{width:24px;height:24px;border-radius:50%;background:var(--red)}
.brand-name{font-size:26px;font-weight:700;color:var(--ink);letter-spacing:-.5px}
.main-nav{left:352px;top:54px;display:flex;height:40px}
.nav-item{border-left:1px solid var(--line);padding:8px 0 0 12px;height:40px}
.nav-item b{display:block;font-weight:400;font-size:11.5px;color:#444}
.nav-item span{display:block;font-size:6.5px;color:#aaa;margin-top:2px}
.header-rule{left:0;top:94px;width:768px;height:6px;background:#f1f1f1}
.hero{left:0;top:100px;width:768px;height:278px;background:linear-gradient(90deg,#cfc7bd 0%,#ece8e2 30%,#f4f2ef 55%,#e6dfd6 75%,#bfb6aa 100%)}
.hero-subject{left:410px;top:100px;width:300px;height:278px;background:radial-gradient(ellipse at 60% 45%,#e05a8c 0%,#d9a3b4 35%,rgba(230,225,220,0) 70%)}
.hero-title{left:74px;top:190px;font-size:23px;line-height:28px;color:var(--ink);font-weight:400}
.hero-title em{font-style:normal;font-weight:700;color:var(--red)}
.slide-btn{top:359px;width:12px;height:12px;background:#333;color:#fff;font-size:9px;line-height:12px;text-align:center}
.feature{top:417px;width:142px}
.feature-img{width:142px;height:81px}
.feature h3{font-size:12.5px;font-weight:400;color:#333;margin:10px 0 6px}
.feature p{font-size:7.3px;line-height:12.5px;color:var(--muted)}
.cta{left:74px;top:597px;width:620px;height:78px;background:var(--panel);border-top:5px solid var(--red);box-shadow:0 2px 4px rgba(0,0,0,.12)}
.cta h2{position:absolute;left:8px;top:24px;font-size:15px;font-weight:400;color:#333}
.cta h2 em{font-style:normal;color:var(--red)}
.cta p{position:absolute;left:8px;top:46px;font-size:7.3px;color:var(--muted)}
.cta-btn{position:absolute;right:0;top:-5px;width:88px;height:78px;background:var(--red);color:#fff;font-size:14.5px;line-height:19px;text-align:center;padding-top:20px}
.section-title{font-size:14px;font-weight:400;color:#333}
.tab-list{left:74px;top:732px;width:92px}
.tab{height:26px;font-size:7.8px;line-height:26px;text-align:center;color:#fff;background:var(--red);margin-bottom:1px}
.tab.active{background:var(--panel);color:#333;border:1px solid var(--line);border-right:none}
.tab-panel{left:166px;top:732px;width:210px;height:171px;border:1px solid var(--line);background:#f6f6f6;padding:8px 10px 0 11px;font-size:7.3px;line-height:12.5px;color:#777}
.tab-img{float:left;width:96px;height:52px;margin:0 10px 4px 2px;background:linear-gradient(135deg,#8a8f94,#2e3236 60%,#d6d9dc)}
.about{left:397px;top:732px;width:297px;font-size:7.3px;line-height:12.5px;color:#666}
.about .lead{color:#333;margin-bottom:12px}
.contact-band{left:0;top:938px;width:768px;height:64px;background:var(--band);border-top:1px solid #ddd;border-bottom:1px solid #ddd;text-align:center;font-size:17px;font-weight:300;color:#444;line-height:62px}
.contact-band b{font-weight:600;color:var(--red)}
.footer{left:0;top:1002px;width:768px;height:198px;background:#f7f7f7}
.footer-about{left:74px;top:1028px;width:290px}
.footer-about p{font-size:7.3px;line-height:10.5px;color:#888;margin:10px 0 8px 2px}
.info-row{display:flex;align-items:center;gap:8px;font-size:7.3px;color:#888;height:23px;padding-left:4px}
.socials{display:flex;gap:5px;margin-top:4px;padding-left:3px}
.social{width:15px;height:15px;border:1px solid #ccc;background:#fff;display:flex;align-items:center;justify-content:center}
.social i{width:6px;height:6px;background:#777;display:block}
.divider{left:376px;top:1028px;width:1px;height:146px;background:var(--line)}
.form-title{left:389px;top:1028px}
.field label{display:block;font-size:6px;color:#555;letter-spacing:.3px}
.field .input{border:1px solid var(--line);background:#fff;margin-top:2px}
.send{left:657px;top:1152px;width:37px;height:16px;background:var(--red);color:#fff;font-size:10px;text-align:center;line-height:16px}
</style>
</head>
<body>
<div class="abs top-bar"></div>
<div class="abs top-toggle">+</div>

<header>
  <div class="abs brand"><span class="brand-mark"></span><span class="brand-name">Hlumo</span></div>
  <nav class="abs main-nav">
    <div class="nav-item" style="width:95px"><b>What We Are</b><span>A lot of features</span></div>
    <div class="nav-item" style="width:104px"><b>What We Offer</b><span>See what we are</span></div>
    <div class="nav-item" style="width:73px"><b>Support</b><span>Read our posts</span></div>
    <div class="nav-item" style="width:72px"><b>Contact Us</b><span>Contact us Today!</span></div>
  </nav>
  <div class="abs header-rule"></div>
</header>

<section>
  <div class="abs hero" role="img" aria-label="Photo of a woman using an office copier in a bright office"></div>
  <div class="abs hero-subject" role="img" aria-label="Woman in a pink top lifting the copier lid"></div>
  <h1 class="abs hero-title"><em>Great</em> with <em>Copiers</em>,<br>Even better&nbsp; with <em>People</em></h1>
  <div class="abs slide-btn" style="left:84px">‹</div>
  <div class="abs slide-btn" style="left:100px">›</div>
</section>

<section>
  <div class="abs feature" style="left:74px">
    <div class="feature-img" role="img" aria-label="Open book on a stack of books" style="background:linear-gradient(180deg,#5a2a12,#c9884a 55%,#7a3b16)"></div>
    <h3>Our Philosophy</h3>
    <p>It is a long established fact that a reaer will be distracted by the readabe cont of a page when looking.</p>
  </div>
  <div class="abs feature" style="left:233px">
    <div class="feature-img" role="img" aria-label="Stacked stones by the sea under a cloudy sky" style="background:linear-gradient(180deg,#6f8fb4,#b8c6d4 55%,#4e5862)"></div>
    <h3>Our Values</h3>
    <p>It is a long established fact that a reaer will be distracted by the readabe cont of a page when looking.</p>
  </div>
  <div class="abs feature" style="left:392px">
    <div class="feature-img" role="img" aria-label="Close-up of dollar and percent keyboard keys" style="background:linear-gradient(180deg,#0b1f7a,#2f5fd6 50%,#9fb6e0)"></div>
    <h3>Bill of Rights</h3>
    <p>It is a long established fact that a reaer will be distracted by the readabe cont of a page when looking.</p>
  </div>
  <div class="abs feature" style="left:551px">
    <div class="feature-img" role="img" aria-label="Golden glass award trophy" style="background:linear-gradient(90deg,#2a1606,#c98a2a 50%,#3a2008)"></div>
    <h3>Awards</h3>
    <p>It is a long established fact that a reaer will be distracted by the readabe cont of a page when looking.</p>
  </div>
</section>

<section class="abs cta">
  <h2>For <em>software</em> and <em>utilities</em></h2>
  <p>If you need drivers for an operating system not listed please contact us.</p>
  <div class="cta-btn">Download<br>Drivers</div>
</section>

<section>
  <h2 class="abs section-title" style="left:75px;top:705px">Tabs</h2>
  <div class="abs tab-list">
    <div class="tab active">Colour Copier</div>
    <div class="tab">Fax Machines</div>
    <div class="tab">Simple Copier</div>
  </div>
  <div class="abs tab-panel">
    <div class="tab-img" role="img" aria-label="Hand pressing a copier control panel"></div>
    It is a long established fact that a reader will be distracted by the readable content of a page when looking at its layout. The point of using Lorem Ipsum is that it has a more-or-less normal distribution of letters, as opposed to using 'Content here, content here', making it look like readable English. Many desktop publishing packages and web page editors now use Lorem Ipsum as their default model text, and a search for 'lorem ipsum' will uncover.
  </div>

  <h2 class="abs section-title" style="left:397px;top:705px">About Us</h2>
  <div class="abs about">
    <p class="lead">Lorem Ipsum is simply dummy text of the printing and typesetting industry. Lorem Ipsum has been the industry's standard dummy text ever since the 1500s, when an unknown printer took a galley of type and scrambled.</p>
    <p>It to make a type specimen book. It has survived not only five centuries, but also the leap into electronic typesetting, remaining essentially unchanged. It was popularised in the 1960s with the release of Tessmark sheets containing Lorem Ipsum passages, and more recently with desktop publishing software like Folio Layout including versions of Lorem Ipsum.It is a long established fact that a reader will be distracted by the readable content of a page when looking at its layout. The point of using Lorem Ipsum is that it has a more-or-less normal distribution of letters, as opposed to using 'Content here, content here', making it look like readable English. Many desktop publishing packages and web page editors now use Lorem Ipsum as their default model text, and a search or 'lorem ipsum'.</p>
  </div>
</section>

<div class="abs contact-band">IF YOU NEED FURTHER INFORMATION <b>CONTACT US</b></div>

<footer>
  <div class="abs footer"></div>
  <div class="abs footer-about">
    <h2 class="section-title" style="font-size:12px">About Us</h2>
    <p>Vel urna amet in augue dapibus. Porta eu, nisi habitasse nec et pellentesque amet?Vel velit dapibus nascetur turpis aenean et. Eros rhoncus elementum diam.</p>
    <div class="info-row">
      <svg width="10" height="12" viewBox="0 0 10 12"><path d="M5 0a4 4 0 0 0-4 4c0 3 4 8 4 8s4-5 4-8a4 4 0 0 0-4-4z" fill="#333"/><circle cx="5" cy="4" r="1.5" fill="#f7f7f7"/></svg>
      Adipiscing elit. Aliquam sed lorem eu leo 1882-377 NY</div>
    <div class="info-row">
      <svg width="10" height="12" viewBox="0 0 10 12"><rect x="2" y="0.5" width="6" height="11" rx="1" fill="none" stroke="#333" stroke-width="1.2"/><rect x="4" y="9" width="2" height="1" fill="#333"/></svg>
      555 0142 7781</div>
    <div class="info-row">
      <svg width="10" height="12" viewBox="0 0 10 12"><circle cx="5" cy="6" r="4.5" fill="#333"/></svg>
      mireldesign</div>
    <div class="socials">
      <div class="social"><i></i></div><div class="social"><i></i></div><div class="social"><i></i></div><div class="social"><i></i></div><div class="social"><i></i></div><div class="social"><i></i></div><div class="social"><i></i></div>
    </div>
  </div>
  <div class="abs divider"></div>
  <h2 class="abs section-title form-title" style="font-size:12px">Contact Us</h2>
  <div class="abs field" style="left:389px;top:1058px"><label>Name</label><div class="input" style="width:126px;height:15px"></div></div>
  <div class="abs field" style="left:389px;top:1090px"><label>Subject</label><div class="input" style="width:126px;height:15px"></div></div>
  <div class="abs field" style="left:389px;top:1122px"><label>Email</label><div class="input" style="width:126px;height:15px"></div></div>
  <div class="abs field" style="left:531px;top:1058px"><label>Message</label><div class="input" style="width:163px;height:79px"></div></div>
  <div class="abs send">Send</div>
</footer>
</body>
</html>
```